依頼詳細
従業員10名以上の企業にマイクロバスレンタカーの利用を促すチラシを配布する事になりました。コロナ終息後に企業の担当者が思わず話を聞いてみたいと思われるチラシの作成をお願い致します。
記載項目
本社:株式会社ミドリヤマ運輸
530-0087
大阪府大阪市北区天満橋5丁目8番2号 桜川フクダビル9階
TEL: 0120-472-915(06-6248-3957) FAX: 06-6248-3951
Mail:info@kazemidori-rent.example.jp
URL:http://www.kazemidori-rent.example.jp

東京支店
東京都千代田区神田須田町4丁目2番7 ルミナス須田ビル3階
TEL:03-5847-2396 FAX:03-5847-2397

サイズ
A4
ページ数
両面
希望イメージ
シンプル 複雑
単色 カラフル
暗い 明るい
日常 高級
遊び心 厳粛
未来的 伝統的
女性的 男性的
希望する色
青系、茶系、無彩色系
納品ファイル
• イラストレーター形式 (.ai)
• フォトショップ形式 (.psd)
補足説明
前回親会社が作成したチラシがありましたので参考までにお送りさせて頂きます。
株式会社ミドリヤマ運輸ロゴです。
チラチ表面・裏面で必ず入れて入れたい情報(改)
会社のロゴやチラシ作成で記載をお願いしたい情報を纏めさせて頂きました。
チラシ作成にあたり、記載をして欲しい事を纏めております。
住所ラベル
【60×105mm】のスペース必須でデザインをよろしくお願い申し上げます。
高級感を醸し出す作品の提供を宜しくお願い致します
弊社は高年式のマイクロバスを多数所有しております。
装備内容も標準装備でこれだけ付いている会社はないと自負しております。
写真追加させていただきます
安全•安心•快適にお過ごし頂く為にドライバーも含めたトータルサポートを
是非この機会にご検討くださいませ。
※違反行為をしている会社と判断をされ、イメージが悪くなる為

マイクロバスは送迎はもちろん、日帰りや1泊2日の観光旅行などにもよく利用されております。
ある種絞り込みをした文面がインパクトある為、送迎に関する事のみ記載

※上記文面に対して社内より問題ありと判断された為、削除をお願い出来ないでしょうか?
お手数お掛け致しますが何卒宜しくお願い致します。
■ 選んだ理由

入選された皆様

いつも大変お世話になっております。
株式会社ミドリヤマ運輸の森下敏彦です。
この度はチラシ作成に尽力頂きありがとうございます。
見やすさ、高級感なおかつレンタカーのイメージがわかりやすいモノを選ばせて頂きました。
最後になりますが入選された作品のai データの送付を宜しくお願い致します。
この度は本当にお疲れ様でした。

■ 提案者全員のお礼・コメント

いつも大変お世話になっております。この度は本当に弊社チラシ作成に尽力を頂きありがとうございます。これからも皆様のお力をお借りすると思いますので引き続き宜しくお願い致します。

```html
<!DOCTYPE html>
<html lang="ja">
<head>
<meta charset="utf-8">
<title>マイクロバス専門レンタカー チラシ</title>
<link href="https://fonts.googleapis.com/css2?family=Noto+Sans+JP:wght@400;500;700;900&family=Shippori+Mincho:wght@500;700;800&display=swap" rel="stylesheet">
<style>
  :root{
    --navy:#1c2f5c;
    --bronze:#a98a5c;
    --bronze-dark:#8c6f45;
    --paper:#ffffff;
    --mist:#ecebe8;
    --ink:#333333;
    --tag:#d9c9ad;
  }
  *{margin:0;padding:0;box-sizing:border-box}
  html,body{width:849px;height:1200px;overflow:hidden;background:var(--paper)}
  body{font-family:"Noto Sans JP",sans-serif;color:var(--ink);position:relative}
  .hero-bg{position:absolute;left:0;top:0;width:849px;height:280px;
    background:linear-gradient(180deg,#dcdad6 0%,#eeedea 70%,#fff 100%)}
  .invite{position:absolute;right:0;top:0;width:380px;height:250px;background:var(--bronze);
    color:#fff;text-align:center;font-family:"Shippori Mincho",serif;padding-top:24px;z-index:2}
  .invite-frame{position:absolute;inset:10px;border:1px solid rgba(255,255,255,.7)}
  .invite .l1{font-size:27px;font-weight:700;letter-spacing:3px}
  .invite .l2{font-size:50px;font-weight:800;line-height:1.3;letter-spacing:2px}
  .invite .l2 .or{display:inline-block;width:34px;height:34px;border-radius:50%;background:#fff;color:var(--bronze);
    font-size:11px;line-height:34px;vertical-align:middle;margin:0 4px;font-family:"Noto Sans JP",sans-serif;letter-spacing:0}
  .invite .l3{font-size:27px;font-weight:700;letter-spacing:3px}
  .invite .note{font-family:"Noto Sans JP",sans-serif;font-size:10px;margin-top:10px}

  .bus-photo{position:absolute;left:360px;top:500px;width:489px;height:360px;
    background:linear-gradient(160deg,#c9ced6 0%,#8e98a8 45%,#eef0f2 100%)}

  .headline{position:absolute;left:40px;top:296px;color:var(--navy);font-weight:900;z-index:2}
  .headline .h1{font-size:60px;letter-spacing:1px;line-height:1.3;white-space:nowrap}
  .headline .h1 big{font-size:76px}
  .headline .h2{font-size:40px;line-height:1.3;white-space:nowrap}
  .headline .h3{font-size:24px;font-weight:700;margin-top:22px;line-height:1.65;white-space:nowrap}

  .perks{position:absolute;left:28px;top:596px;display:grid;grid-template-columns:repeat(3,102px);gap:8px;z-index:2}
  .perk{height:116px;background:var(--bronze);color:#fff;text-align:center;padding-top:8px;font-weight:700}
  .perk svg{display:block;margin:0 auto 4px}
  .perk .s{font-size:12px;line-height:1.35}
  .perk .b{font-size:20px;line-height:1.2}

  .caption{position:absolute;left:28px;top:846px;font-size:15px;font-weight:700;color:var(--bronze-dark);
    border-bottom:1px solid var(--bronze);padding-bottom:3px}

  .services{position:absolute;left:28px;top:888px;width:793px;display:grid;grid-template-columns:1fr 1fr;column-gap:30px;row-gap:16px}
  .service h3{font-family:"Shippori Mincho",serif;font-size:19px;color:var(--navy);font-weight:800;
    border-top:3px solid var(--bronze);border-bottom:1px solid var(--bronze);background:var(--mist);padding:5px 10px}
  .service p{font-size:12px;line-height:1.65;margin-top:7px}
  .tags{display:grid;grid-template-columns:repeat(3,1fr);gap:5px;margin-top:7px}
  .tags span{background:var(--tag);color:var(--bronze-dark);font-size:11px;text-align:center;padding:3px 0}
</style>
</head>
<body>
  <div class="hero-bg"></div>

  <section class="invite">
    <div class="invite-frame"></div>
    <div class="l1">レンタカー送迎を</div>
    <div class="l2">導入<span class="or">または</span>検討</div>
    <div class="l3">されている皆様へ</div>
    <div class="note">コスト削減と業務化を図るご提案をさせて頂きます。</div>
  </section>

  <div class="bus-photo" role="img" aria-label="白いマイクロバスが並ぶ写真"></div>

  <header class="headline">
    <div class="h1">マイクロバス<big>専門</big>の</div>
    <div class="h2">レンタカー会社だからこそ、</div>
    <div class="h3">マイクロバスに関する様々な問題と課題を<br>解決致します。</div>
  </header>

  <div class="perks">
    <div class="perk"><svg width="28" height="24" viewBox="0 0 34 30"><rect x="3" y="5" width="28" height="23" fill="none" stroke="#fff" stroke-width="2"/><line x1="3" y1="11" x2="31" y2="11" stroke="#fff" stroke-width="2"/></svg><div class="s">土日祝でも</div><div class="b">平日料金</div></div>
    <div class="perk"><svg width="28" height="24" viewBox="0 0 34 30"><rect x="5" y="3" width="24" height="25" fill="none" stroke="#fff" stroke-width="2"/><line x1="10" y1="10" x2="24" y2="10" stroke="#fff" stroke-width="2"/><line x1="10" y1="16" x2="24" y2="16" stroke="#fff" stroke-width="2"/></svg><div class="s">レンタル料金は</div><div class="b">保険料込</div></div>
    <div class="perk"><svg width="28" height="24" viewBox="0 0 34 30"><rect x="4" y="6" width="26" height="18" fill="none" stroke="#fff" stroke-width="2"/></svg><div class="s">ナビ･ETC<br>バックモニター</div><div class="b">標準装備</div></div>
    <div class="perk"><svg width="28" height="24" viewBox="0 0 34 30"><circle cx="17" cy="15" r="12" fill="none" stroke="#fff" stroke-width="2"/><line x1="9" y1="7" x2="25" y2="23" stroke="#fff" stroke-width="2"/></svg><div class="s">すべて</div><div class="b">禁煙車</div></div>
    <div class="perk"><svg width="28" height="24" viewBox="0 0 34 30"><rect x="6" y="8" width="22" height="18" fill="none" stroke="#fff" stroke-width="2"/><line x1="17" y1="2" x2="17" y2="8" stroke="#fff" stroke-width="2"/></svg><div class="s">車内の</div><div class="b">消臭・<br>芳香加工</div></div>
    <div class="perk"><svg width="28" height="24" viewBox="0 0 34 30"><path d="M8 26 Q4 16 12 10 M17 26 Q13 16 21 10 M26 26 Q22 16 30 10" fill="none" stroke="#fff" stroke-width="2"/></svg><div class="s">高温スチームで</div><div class="b">シートを<br>抗菌</div></div>
  </div>

  <p class="caption">清掃はもちろんアルコール除菌も毎回行っております</p>

  <div class="services">
    <section class="service">
      <h3>運行企画立案のご提供</h3>
      <p>送迎を始める前のアンケートや時刻表などの作成準備から運行ルートや停車場所の設定、送迎開始後の見直しまで運行企画をサポート致します。</p>
    </section>
    <section class="service">
      <h3>送迎バスの運行管理会社のご紹介</h3>
      <p>業務用車両の管理事業者と提携しており、運転手派遣や運行管理も含めたご提案が可能です。送迎に関する業務を一括でお任せいただけます。</p>
    </section>
    <section class="service">
      <h3>今すぐ送迎バスが必要</h3>
      <p>急な利用にも柔軟に対応致します。こんな方にぜひご相談ください。</p>
      <div class="tags"><span>スポット短期</span><span>長期契約</span><span>自社運行</span><span>台数追加</span><span>車両入替</span><span>臨時便</span></div>
    </section>
    <section class="service">
      <h3>所有車両を買い取らせていただきます</h3>
      <p>どんなクルマでもご相談下さい。自社で保有する車両の買取とレンタル切替でコスト削減を実現致します。</p>
    </section>
  </div>
</body>
</html>
```